Corvane wall and floor tiling

I would like you to design me a wrap for my work van, I will provide the logo I would like you to work off.
I’m happy for some slight little changes.
just need some creativity with the wrap design & background.
We are a tiling business in the construction industry.
Any designs are welcome but I do like what I have going on here and this type of font.
Show me what you got.
I would like the van to have a half wrap not just the side stickers like it shows in the photos.
The new mobile numbers I would like on the wrap are
0491638425
0412864359
We cover Tiling, screeding , waterproofing

Industry/Entity Type

Construction

Colors

Designer to choose colors to be used in the design.

Requirements
Must have
• Brindlo & snapveil logo somewhere small. Tiling, Waterproofing & Screeding

```html
<!DOCTYPE html>
<html lang="en">
<head>
<meta charset="utf-8">
<title>Corvane Wall &amp; Floor Tiling – Van Wrap</title>
<link href="https://fonts.googleapis.com/css2?family=Poppins:wght@500;700;800&display=swap" rel="stylesheet">
<style>
  :root{
    --page:#ffffff;
    --wrap-black:#1d1e21;
    --wrap-blue:#1e9be0;
    --body-white:#eef0f2;
    --glass:#8d9096;
    --tyre:#1a1a1a;
    --rim:#c9ccd1;
    --trim:#2a2b2e;
    --light-red:#b3262b;
    --text-white:#ffffff;
  }
  html,body{margin:0;padding:0;overflow:hidden;background:var(--page);}
  .sheet{width:1200px;height:1200px;position:relative;overflow:hidden;background:var(--page);}
  .sheet svg{display:block;width:1200px;height:1200px;}
  .brand{font-family:'Poppins',sans-serif;font-weight:800;fill:var(--wrap-blue);letter-spacing:1px;}
  .tagline{font-family:'Poppins',sans-serif;font-weight:800;fill:var(--wrap-blue);}
  .services{font-family:'Poppins',sans-serif;font-weight:700;fill:var(--text-white);font-size:10.5px;}
  .services-dark{font-family:'Poppins',sans-serif;font-weight:700;fill:var(--wrap-black);font-size:9px;}
  .phone{font-family:'Poppins',sans-serif;font-weight:700;letter-spacing:1.5px;}
  .phone-blue{fill:var(--wrap-blue);}
  .phone-white{fill:var(--text-white);}
  .social{font-family:'Poppins',sans-serif;font-weight:700;fill:var(--text-white);font-size:7px;}
  .plate{font-family:'Poppins',sans-serif;font-weight:700;fill:#ffffff;font-size:7px;}
  .blackbody{fill:var(--wrap-black);}
  .whitebody{fill:var(--body-white);}
  .blue{fill:var(--wrap-blue);}
  .glass{fill:var(--glass);}
  .tyre{fill:var(--tyre);}
  .rim{fill:var(--rim);}
  .trim{fill:var(--trim);}
</style>
</head>
<body>
<main class="sheet">
<svg viewBox="0 0 960 960" xmlns="http://www.w3.org/2000/svg" aria-label="Corvane Wall and Floor Tiling van wrap layouts">
  <defs>
    <path id="van-side-body" d="M190,62 Q190,45 212,45 L700,45 Q728,47 742,78 L768,138 Q790,148 790,172 L790,246 Q790,262 772,262 L196,262 Q183,262 183,246 Z"/>
    <clipPath id="clip-van-side"><use href="#van-side-body"/></clipPath>

    <g id="van-side">
      <use href="#van-side-body" class="whitebody"/>
      <g clip-path="url(#clip-van-side)">
        <polygon class="blackbody" points="180,40 235,40 800,100 800,275 605,275 605,250 180,196"/>
        <polygon class="blue" points="180,38 250,38 800,96 800,104 240,44 180,44"/>
        <polygon class="blue" points="180,150 605,205 605,213 180,158"/>
        <polygon class="blue" points="180,182 605,236 605,250 180,196"/>
        <polygon class="blue" points="740,92 800,96 800,104"/>
        <rect class="trim" x="180" y="248" width="620" height="16"/>
      </g>
      <polygon class="glass" points="604,62 712,62 738,124 604,124"/>
      <rect class="trim" x="772" y="176" width="18" height="22" rx="3"/>
      <rect class="trim" x="180" y="140" width="6" height="40" rx="2"/>
      <rect x="180" y="142" width="5" height="30" fill="var(--light-red)"/>
      <ellipse class="trim" cx="310" cy="262" rx="46" ry="40"/>
      <ellipse class="trim" cx="655" cy="262" rx="46" ry="40"/>
      <circle class="tyre" cx="310" cy="265" r="37"/>
      <circle class="rim" cx="310" cy="265" r="24"/>
      <circle class="tyre" cx="655" cy="265" r="37"/>
      <circle class="rim" cx="655" cy="265" r="24"/>
      <ellipse cx="485" cy="305" rx="290" ry="6" fill="#d8d9db"/>
    </g>
  </defs>

  <!-- Side view, facing right -->
  <g class="van-side-right">
    <use href="#van-side"/>
    <g transform="rotate(5 400 130)">
      <rect class="blue" x="200" y="72" width="56" height="56"/>
      <text class="brand" x="272" y="122" font-size="50">CORVANE</text>
      <text class="tagline" x="322" y="150" font-size="17">WALL &amp; FLOOR TILING</text>
      <text class="services" x="202" y="174">TILING • SCREEDING • WATERPROOFING • BATHROOM RENO'S</text>
    </g>
    <circle cx="640" cy="160" r="3" fill="var(--wrap-blue)"/>
    <text class="social" x="646" y="163">Brindlo</text>
    <circle cx="684" cy="160" r="3" fill="var(--wrap-blue)"/>
    <text class="social" x="690" y="163">snapveil</text>
    <text class="phone phone-blue" x="627" y="178" font-size="13">0491 638 425</text>
    <text class="phone phone-white" x="627" y="195" font-size="13">0412 864 359</text>
  </g>

  <!-- Side view, facing left -->
  <g class="van-side-left">
    <use href="#van-side" transform="translate(965,326) scale(-1,1)"/>
    <g transform="rotate(-5 560 460)">
      <text class="brand" x="440" y="462" font-size="50">CORVANE</text>
      <rect class="blue" x="672" y="420" width="56" height="56" transform="translate(-302,18)"/>
      <text class="tagline" x="488" y="490" font-size="17">WALL &amp; FLOOR TILING</text>
      <text class="services" x="372" y="519">TILING • SCREEDING • WATERPROOFING • BATHROOM RENO'S</text>
    </g>
    <circle cx="225" cy="483" r="3" fill="var(--wrap-blue)"/>
    <text class="social" x="231" y="486">Brindlo</text>
    <circle cx="268" cy="483" r="3" fill="var(--wrap-blue)"/>
    <text class="social" x="274" y="486">snapveil</text>
    <text class="phone phone-blue" x="222" y="502" font-size="13">0491 638 425</text>
    <text class="phone phone-white" x="222" y="519" font-size="13">0412 864 359</text>
  </g>

  <!-- Rear view, white door -->
  <g class="van-rear-white">
    <path class="whitebody" d="M82,700 Q84,684 104,684 L286,684 Q306,684 308,700 L312,880 L78,880 Z"/>
    <rect class="blackbody" x="92" y="694" width="206" height="96" rx="6"/>
    <rect x="168" y="687" width="54" height="5" rx="2" fill="var(--light-red)"/>
    <rect class="blue" x="178" y="704" width="28" height="28" transform="translate(0,0)"/>
    <text class="brand" x="195" y="758" font-size="25" text-anchor="middle">CORVANE</text>
    <text class="tagline" x="195" y="775" font-size="11" text-anchor="middle">WALL &amp; FLOOR TILING</text>
    <rect class="blackbody" x="88" y="795" width="214" height="17"/>
    <text class="phone phone-blue" x="92" y="808" font-size="11" letter-spacing="0.5">0491 638 425</text>
    <text class="phone phone-blue" x="206" y="808" font-size="11" letter-spacing="0.5">0412 864 359</text>
    <text class="services-dark" x="96" y="824" font-size="6">KESTRA</text>
    <circle class="blue" cx="114" cy="836" r="6"/>
    <circle class="blackbody" cx="268" cy="836" r="6"/>
    <text class="services-dark" x="195" y="866" text-anchor="middle">TILING | SCREEDING</text>
    <text class="services-dark" x="195" y="877" text-anchor="middle">WATERPROOFING | BATHROOM RENO'S</text>
    <rect x="78" y="782" width="8" height="46" rx="2" fill="var(--light-red)"/>
    <rect x="304" y="782" width="8" height="46" rx="2" fill="var(--light-red)"/>
    <rect class="blackbody" x="76" y="880" width="238" height="22" rx="4"/>
    <ellipse cx="195" cy="910" rx="118" ry="4" fill="#d8d9db"/>
  </g>

  <!-- Rear view, black door -->
  <g class="van-rear-black">
    <path class="blackbody" d="M372,700 Q374,684 394,684 L576,684 Q596,684 598,700 L602,880 L368,880 Z"/>
    <rect x="458" y="687" width="54" height="5" rx="2" fill="var(--light-red)"/>
    <rect class="blue" x="471" y="704" width="28" height="28"/>
    <text class="brand" x="485" y="758" font-size="25" text-anchor="middle">CORVANE</text>
    <text class="tagline" x="485" y="775" font-size="11" text-anchor="middle">WALL &amp; FLOOR TILING</text>
    <rect class="blue" x="378" y="794" width="214" height="2"/>
    <text class="phone phone-blue" x="382" y="808" font-size="11" letter-spacing="0.5">0491 638 425</text>
    <text class="phone phone-blue" x="496" y="808" font-size="11" letter-spacing="0.5">0412 864 359</text>
    <rect class="blue" x="378" y="812" width="214" height="2"/>
    <text class="plate" x="386" y="824" font-size="6">KESTRA</text>
    <circle class="blue" cx="404" cy="836" r="6"/>
    <circle class="blue" cx="558" cy="836" r="6"/>
    <rect class="whitebody" x="378" y="852" width="214" height="28"/>
    <text class="services-dark" x="485" y="866" text-anchor="middle">TILING | SCREEDING</text>
    <text class="services-dark" x="485" y="877" text-anchor="middle">WATERPROOFING | BATHROOM RENO'S</text>
    <rect x="368" y="782" width="8" height="46" rx="2" fill="var(--light-red)"/>
    <rect x="594" y="782" width="8" height="46" rx="2" fill="var(--light-red)"/>
    <rect class="blackbody" x="366" y="880" width="238" height="22" rx="4"/>
    <ellipse cx="485" cy="910" rx="118" ry="4" fill="#d8d9db"/>
  </g>

  <!-- Front view -->
  <g class="van-front">
    <path class="blackbody" d="M650,700 Q652,684 672,684 L858,684 Q878,684 880,700 L888,880 L642,880 Z"/>
    <path class="glass" d="M664,694 L866,694 L876,748 L654,748 Z"/>
    <rect x="628" y="738" width="20" height="16" rx="3" class="trim"/>
    <rect x="882" y="738" width="20" height="16" rx="3" class="trim"/>
    <polygon class="blue" points="650,752 880,752 880,758 650,758"/>
    <rect class="blue" x="678" y="762" width="20" height="20"/>
    <text class="brand" x="706" y="778" font-size="17">CORVANE</text>
    <text class="tagline" x="737" y="790" font-size="8">WALL &amp; FLOOR TILING</text>
    <rect x="652" y="800" width="44" height="20" rx="4" fill="#d7dade"/>
    <rect x="834" y="800" width="44" height="20" rx="4" fill="#d7dade"/>
    <rect class="trim" x="702" y="804" width="126" height="22" rx="3"/>
    <ellipse cx="765" cy="815" rx="10" ry="6" fill="#d7dade"/>
    <rect class="trim" x="676" y="840" width="178" height="26" rx="3"/>
    <rect x="735" y="872" width="60" height="14" fill="#111"/>
    <text class="plate" x="765" y="882" text-anchor="middle">KESTRA</text>
    <rect class="tyre" x="650" y="880" width="30" height="26" rx="4"/>
    <rect class="tyre" x="850" y="880" width="30" height="26" rx="4"/>
    <ellipse cx="765" cy="910" rx="122" ry="4" fill="#d8d9db"/>
  </g>
</svg>
</main>
</body>
</html>
```